New Gay dating app for meeting new people

I am looking for someone to design me a new gay dating app. It should have features such as a sign in page, being able to upload pictures, make a profile, and be able to know the distance from someone and be able to send a location.

Could you please provide the finished product CODED and ready for use.

The colours are up to the designer.

The name of the app LumaVox

If you need to ask me any questions don't hesitate to ask me for anything.

Target Market(s)

Gay males 18+ years old

Industry/Entity Type

Dating

Requirements
Must have
• Be able to chat

```html
<!DOCTYPE html>
<html lang="en">
<head>
<meta charset="utf-8">
<title>LumaVox – Profile</title>
<link rel="stylesheet" href="https://fonts.googleapis.com/css2?family=Open+Sans:wght@300;400;600&display=swap">
<style>
  :root {
    --screen-bg: #2c3745;
    --bar-bg: #28323f;
    --tab-bg: #222b36;
    --text: #c7cdd6;
    --text-dim: #7f8a99;
    --rule: #435061;
    --accent: #a9c64c;
    --avatar-a: #b89a86;
    --avatar-b: #5a4a42;
  }
  * { box-sizing: border-box; margin: 0; padding: 0; }
  html, body {
    width: 753px; height: 1200px; overflow: hidden;
    background: var(--screen-bg);
    font-family: "Open Sans", Arial, sans-serif;
    color: var(--text);
  }
  .app { position: relative; width: 753px; height: 1200px; }

  .status-bar {
    position: absolute; top: 0; left: 0; right: 0; height: 36px;
    background: var(--bar-bg);
    display: flex; align-items: center; justify-content: space-between;
    padding: 0 18px; font-size: 15px; font-weight: 400; color: var(--text-dim);
  }
  .status-bar .carrier { display: flex; align-items: center; gap: 8px; }
  .status-bar .dots { letter-spacing: 2px; }
  .status-bar .battery { display: flex; align-items: center; gap: 6px; }
  .status-bar .battery-box { width: 26px; height: 12px; border: 1.5px solid var(--text-dim); border-radius: 2px; position: relative; }
  .status-bar .battery-box::after { content: ""; position: absolute; inset: 2px; background: var(--text-dim); }

  .nav-bar {
    position: absolute; top: 36px; left: 0; right: 0; height: 86px;
    background: var(--bar-bg);
    display: flex; align-items: center; justify-content: center;
  }
  .nav-bar .title { font-size: 32px; font-weight: 300; color: var(--text-dim); }
  .nav-bar .back { position: absolute; left: 32px; top: 28px; }
  .nav-bar .menu { position: absolute; right: 30px; top: 30px; }

  .avatar {
    position: absolute; left: 50%; top: 176px; width: 184px; height: 184px;
    margin-left: -92px; border-radius: 50%;
    border: 3px solid #dfe3e8;
    background: radial-gradient(circle at 50% 40%, var(--avatar-a), var(--avatar-b));
  }

  .profile-form { position: absolute; left: 77px; right: 90px; top: 400px; }
  .field {
    height: 134px; display: flex; align-items: center; justify-content: center;
    border-bottom: 1.5px solid var(--rule);
    font-size: 26px; font-weight: 300; color: var(--text);
  }
  .field:first-child { height: 92px; }

  .submit-button {
    position: absolute; left: 50%; top: 980px; width: 300px; height: 58px;
    margin-left: -150px; border: 2px solid var(--accent); border-radius: 29px;
    background: transparent; color: var(--accent);
    font-family: "Open Sans", Arial, sans-serif; font-size: 20px; font-weight: 400;
    letter-spacing: 1px; text-transform: uppercase;
  }

  .tab-bar {
    position: absolute; left: 0; right: 0; bottom: 0; height: 90px;
    background: var(--tab-bg);
    display: flex; align-items: center; justify-content: space-between;
    padding: 0 62px;
  }
</style>
</head>
<body>
<main class="app">
  <header class="status-bar">
    <div class="carrier"><span class="dots">●●●○○</span><span>VOXTEL</span></div>
    <div class="time">4:21 PM</div>
    <div class="battery"><span>100%</span><span class="battery-box"></span></div>
  </header>

  <nav class="nav-bar">
    <svg class="back" width="20" height="32" viewBox="0 0 20 32"><polyline points="17,2 3,16 17,30" fill="none" stroke="#7f8a99" stroke-width="2.5"/></svg>
    <h1 class="title">Profile</h1>
    <svg class="menu" width="40" height="26" viewBox="0 0 40 26"><g stroke="#7f8a99" stroke-width="2.5"><line x1="0" y1="2" x2="40" y2="2"/><line x1="0" y1="13" x2="40" y2="13"/><line x1="0" y1="24" x2="40" y2="24"/></g></svg>
  </nav>

  <div class="avatar" role="img" aria-label="Profile photo of the user"></div>

  <form class="profile-form">
    <div class="field">Username</div>
    <div class="field">Password</div>
    <div class="field">Age</div>
    <div class="field">Location</div>
  </form>

  <button class="submit-button" type="button">Submit</button>

  <footer class="tab-bar">
    <svg width="44" height="44" viewBox="0 0 44 44" aria-label="Profile"><g fill="none" stroke="#aab3bf" stroke-width="2.2"><circle cx="22" cy="14" r="9"/><path d="M4 42 C4 30 12 25 22 25 C32 25 40 30 40 42 Z"/></g></svg>
    <svg width="44" height="44" viewBox="0 0 44 44" aria-label="Chat"><g fill="none" stroke="#a9c64c" stroke-width="2.2"><path d="M22 4 C33 4 40 11 40 20 C40 29 33 36 22 36 C19 36 16 35 14 34 L5 39 L8 31 C5 28 4 24 4 20 C4 11 11 4 22 4 Z"/><line x1="14" y1="17" x2="30" y2="17"/><line x1="14" y1="24" x2="26" y2="24"/></g></svg>
    <svg width="44" height="44" viewBox="0 0 44 44" aria-label="Favourites"><polygon points="22,3 27.6,16 41,16.5 30.5,25 34,39 22,31 10,39 13.5,25 3,16.5 16.4,16" fill="none" stroke="#aab3bf" stroke-width="2.2" stroke-linejoin="round"/></svg>
  </footer>
</main>
</body>
</html>
```